FSA Expiring Soon 2023

Hi,
Looking to upgrade the design of current flyer to be used as an e-blast.
-8.5"x11"
-Under 5MB
-Several formats, PDF, .ai, jpeg, png

This flyer should be simple, yet eye catching. The goal is to remind patients that their Flexible Spending Account (FSA) will be expiring soon and that they can use their FSA or HSA to purchase most of our over the counter items, including inserts and shoes.

-must include: Some insurance plans require a letter of medical necessity
-must include: Each flexible spending account varies on their expiration date
- stock images must be free

I'll attach our logo and old flyer as well for reference.

Thank you,
Oscar

```html
<!DOCTYPE html>
<html lang="en">
<head>
<meta charset="utf-8">
<title>FSA Expiring Soon – Linden Foot &amp; Ankle</title>
<link rel="stylesheet" href="https://fonts.googleapis.com/css2?family=Montserrat:wght@400;500;600;700;800&display=swap">
<style>
  :root {
    --orange: #f5814f;
    --orange-dark: #d9683d;
    --orange-band: #f88455;
    --teal: #3aae8d;
    --teal-bright: #45bca5;
    --teal-dark: #2f9d86;
    --ink: #333333;
    --paper: #ffffff;
    --backdrop: #e9e9e9;
  }
  * { box-sizing: border-box; margin: 0; padding: 0; }
  html, body {
    width: 960px; height: 1200px; overflow: hidden;
    background: var(--backdrop);
    font-family: "Montserrat", Arial, sans-serif;
  }
  .flyer {
    position: absolute; left: 40px; top: 30px;
    width: 880px; height: 1140px;
    background: var(--paper);
    overflow: hidden;
  }
  .abs { position: absolute; }

  /* brand block */
  .brand-dot {
    left: 78px; top: 48px; width: 130px; height: 130px;
    border-radius: 50%; background: var(--teal-bright);
  }
  .brand-name {
    right: 54px; top: 14px; text-align: right;
    color: var(--orange); font-weight: 800;
    font-size: 70px; line-height: 76px; letter-spacing: -0.5px;
    white-space: nowrap;
  }
  .brand-site {
    right: 54px; top: 168px;
    color: var(--orange); font-weight: 800; font-size: 28px;
  }

  /* ribbon */
  .ribbon { left: 309px; top: 248px; width: 262px; height: 160px; overflow: visible; }
  .ribbon text { font-family: "Montserrat", Arial, sans-serif; font-weight: 600; fill: #fff; }

  /* messages */
  .headline {
    left: 0; width: 100%; top: 413px; text-align: center;
    color: var(--ink); font-weight: 700; font-size: 30px; line-height: 38px;
  }
  .photo {
    left: 185px; top: 495px; width: 505px; height: 211px;
    background: linear-gradient(180deg, #7f9f68 0%, #a5b88e 35%, #d9d4c2 60%, #c9ccd0 100%);
  }
  .eligible {
    left: 0; width: 100%; top: 713px; text-align: center;
    color: var(--ink); font-weight: 700; font-size: 25.5px; line-height: 29px;
  }
  .notes {
    left: 0; width: 100%; top: 775px; text-align: center;
    color: var(--ink); font-weight: 400; font-size: 19.5px; line-height: 28px;
  }
  .cta {
    left: 222px; top: 842px; width: 433px; height: 57px;
    background: var(--orange); color: #fff;
    font-weight: 700; font-size: 26px; letter-spacing: 0.3px;
    display: flex; align-items: center; justify-content: center;
  }
  .offices-title {
    left: 0; width: 100%; top: 906px; text-align: center;
    color: var(--orange); font-weight: 700; font-size: 24px;
  }

  /* offices band */
  .offices-band { left: 0; top: 945px; width: 100%; height: 133px; background: var(--orange-band); }
  .office-label {
    top: 14px; height: 31px; background: #fff;
    display: flex; align-items: center;
    color: var(--teal); font-weight: 700; font-size: 16px;
    padding-left: 36px; white-space: nowrap;
  }
  .office-pin {
    position: absolute; left: -4px; top: -4px; width: 39px; height: 39px;
    border-radius: 50%; background: #fff; border: 2px solid var(--orange-band);
    display: flex; align-items: center; justify-content: center;
  }
  .office-address {
    top: 57px; color: #fff; font-weight: 500; font-size: 15px; line-height: 20.5px;
    white-space: nowrap;
  }

  /* contact band */
  .contact-band {
    left: 0; top: 1078px; width: 100%; height: 62px; background: var(--teal);
    color: #fff; font-weight: 700; font-size: 28px;
  }
  .contact-item { top: 0; height: 62px; display: flex; align-items: center; gap: 6px; }
</style>
</head>
<body>
  <main class="flyer">
    <header>
      <div class="abs brand-dot" aria-hidden="true"></div>
      <h1 class="abs brand-name">LINDEN<br>FOOT &amp; ANKLE</h1>
      <div class="abs brand-site">STEADYSTRIDE.COM</div>
    </header>

    <svg class="abs ribbon" viewBox="0 0 262 160" aria-label="Expiring soon">
      <polygon points="0,100 30,98 0,135" fill="var(--orange-dark)"/>
      <polygon points="0,32 229,1 229,72 0,104" fill="var(--orange)"/>
      <text x="20" y="84" font-size="36" transform="rotate(-9 20 84)">EXPIRING</text>
      <polygon points="240,136 262,136 262,152" fill="var(--teal-dark)"/>
      <polygon points="102,92 262,67 262,136 102,154" fill="var(--teal-bright)"/>
      <text x="124" y="138" font-size="37" transform="rotate(-8 124 138)">SOON</text>
    </svg>

    <p class="abs headline">Use your Flexible Spending Account funds<br>before they expire at the end of the year!</p>

    <div class="abs photo" role="img" aria-label="Photo of three wooden blocks spelling FSA on a table with a blurred green background"></div>

    <p class="abs eligible">Most of our over the counter products are FSA/HSA<br>eligible, including orthotics and shoes.</p>
    <p class="abs notes">(Some insurance plans require a letter of medical necessity)<br>Each flexible spending account varies on their expiration date</p>

    <div class="abs cta">REQUEST AN APPOINTMENT</div>
    <h2 class="abs offices-title">OUR OFFICES</h2>

    <section class="abs offices-band">
      <div class="abs office-label" style="left:41px;width:220px;">
        <span class="office-pin"><svg width="16" height="22" viewBox="0 0 16 22"><path d="M8 0C3.6 0 0 3.5 0 7.9 0 13.5 8 22 8 22s8-8.5 8-14.1C16 3.5 12.4 0 8 0z" fill="var(--teal)"/><circle cx="8" cy="8" r="3.2" fill="#fff"/></svg></span>LINDEN OFFICE
      </div>
      <p class="abs office-address" style="left:62px;">218 Alder Crest Dr.<br>Ste. 140<br>Linden, MD 21790</p>

      <div class="abs office-label" style="left:323px;width:220px;">
        <span class="office-pin"><svg width="16" height="22" viewBox="0 0 16 22"><path d="M8 0C3.6 0 0 3.5 0 7.9 0 13.5 8 22 8 22s8-8.5 8-14.1C16 3.5 12.4 0 8 0z" fill="var(--teal)"/><circle cx="8" cy="8" r="3.2" fill="#fff"/></svg></span>BROOKVALE OFFICE
      </div>
      <p class="abs office-address" style="left:350px;">5120 Meadowlark Blvd.<br>Ste. 305<br>Brookvale, MD 21795</p>

      <div class="abs office-label" style="left:588px;width:253px;">
        <span class="office-pin"><svg width="16" height="22" viewBox="0 0 16 22"><path d="M8 0C3.6 0 0 3.5 0 7.9 0 13.5 8 22 8 22s8-8.5 8-14.1C16 3.5 12.4 0 8 0z" fill="var(--teal)"/><circle cx="8" cy="8" r="3.2" fill="#fff"/></svg></span>HARLOW OFFICE
      </div>
      <p class="abs office-address" style="left:624px;">77 Wellness Way<br>Harlow, WV&nbsp; 25499</p>
    </section>

    <footer class="abs contact-band">
      <div class="abs contact-item" style="left:67px;">
        <svg width="24" height="24" viewBox="0 0 24 24" fill="none" stroke="#fff" stroke-width="1.5"><circle cx="12" cy="12" r="10.5"/><circle cx="12" cy="12" r="6.5"/><ellipse cx="12" cy="12" rx="3" ry="6.5"/><line x1="5.5" y1="12" x2="18.5" y2="12"/><line x1="6.5" y1="9" x2="17.5" y2="9"/><line x1="6.5" y1="15" x2="17.5" y2="15"/></svg>
        Steadystride.com
      </div>
      <div class="abs contact-item" style="left:543px;">
        <svg width="26" height="26" viewBox="0 0 26 26" fill="none" stroke="#fff" stroke-width="1.5"><circle cx="13" cy="13" r="12"/><path d="M9 7.5l2 3-1.3 1.4c.8 1.8 2.3 3.3 4.1 4.1L15.2 14.7l3 2-1 2.2c-4.8-.4-8.7-4.3-9.2-9.2z"/></svg>
        877-555-0142
      </div>
    </footer>
  </main>
</body>
</html>
```